Cutting Board Oil Label

I would like a label created for our custom made cutting board oil. The bottle will be clear and come in several different sizes. I have included the current label we use. We would like the information to stay the same, but more aesthetically pleasing and professionally presented. I am also including our logo and the current label of our biggest competitor.

```html
<!DOCTYPE html>
<html lang="en">
<head>
<meta charset="utf-8">
<title>Cutting Board Conditioner Label</title>
<link rel="stylesheet" href="https://fonts.googleapis.com/css2?family=Montserrat:wght@400;500;600;700&display=swap">
<style>
  :root {
    --canvas-bg: #f6f6f6;
    --label-bg: #ffffff;
    --band: #47484a;
    --ink: #4a4a4a;
    --teal: #3fb3bb;
    --panel: #c9cacc;
    --white: #ffffff;
  }
  * { margin: 0; padding: 0; box-sizing: border-box; }
  html, body {
    width: 1200px;
    height: 1000px;
    overflow: hidden;
    background: var(--canvas-bg);
    font-family: "Montserrat", Arial, sans-serif;
  }
  .canvas {
    width: 1200px;
    height: 1000px;
    display: flex;
    align-items: center;
    justify-content: center;
  }
  .label {
    width: 560px;
    background: var(--label-bg);
    padding: 60px 0 56px;
    display: flex;
    flex-direction: column;
    align-items: center;
    text-align: center;
  }
  .brand {
    display: flex;
    align-items: center;
    gap: 12px;
    margin-bottom: 28px;
  }
  .brand-dot {
    width: 22px;
    height: 22px;
    border-radius: 50%;
    background: var(--teal);
  }
  .brand-name {
    font-size: 30px;
    font-weight: 500;
    color: var(--ink);
  }
  .title-band {
    width: 100%;
    background: var(--band);
    padding: 24px 44px 30px;
    color: var(--white);
  }
  .title-main {
    font-size: 50px;
    font-weight: 500;
    letter-spacing: 1px;
    line-height: 1.1;
  }
  .title-sub {
    font-size: 42px;
    font-weight: 400;
    letter-spacing: 9px;
    line-height: 1.15;
  }
  .title-rule {
    height: 3px;
    background: var(--teal);
    margin: 12px 0 14px;
  }
  .usage {
    font-size: 16px;
    line-height: 1.35;
    margin-bottom: 18px;
  }
  .ingredients {
    background: var(--panel);
    color: #222;
    font-size: 15px;
    font-weight: 700;
    line-height: 1.4;
    padding: 8px 14px;
    border: 1px solid #e2e2e2;
  }
  .claims {
    margin-top: 22px;
    font-size: 24px;
    font-weight: 600;
    letter-spacing: 2px;
    color: var(--teal);
    word-spacing: 6px;
  }
  .origin {
    margin-top: 12px;
    font-size: 15px;
    font-weight: 600;
    color: var(--ink);
  }
  .website {
    margin-top: 14px;
    font-size: 15px;
    font-weight: 600;
    color: var(--ink);
  }
</style>
</head>
<body>
  <main class="canvas">
    <section class="label">
      <div class="brand">
        <span class="brand-dot"></span>
        <span class="brand-name">Cedar Hollow Goods</span>
      </div>
      <div class="title-band">
        <div class="title-main">CUTTING BOARD</div>
        <div class="title-sub">conditioner</div>
        <div class="title-rule"></div>
        <p class="usage">For use on cutting boards, butcher blocks, wood utensils, and any other wood products.</p>
        <p class="ingredients">Made with: Beeswax, Mineral Oil, Orange Oil,<br>Lemon Oil, and Vitamin E</p>
      </div>
      <p class="claims">FOOD SAFE &nbsp; - &nbsp; ALL NATURAL</p>
      <p class="origin">Made in the USA</p>
      <p class="website">www.CedarHollowGoods.com</p>
    </section>
  </main>
</body>
</html>
```